Business card design needed

I need a business card design for a dog walking, dog minding and dog training business. Please refer to my website for the basic company colours and fonts I'm after. Planning on a double sided card, so all information doesn't need to be on the 'front' side.
Cheers

Industry/Entity Type

Dog Training

Contact Information for Business Card

Meadow Paws - happy hounds
Rua 0498307164
meadowpawsdemo.com.au
-walking
-holiday stays
-onsite care
-training and behavioural consultations

```html
<!DOCTYPE html>
<html lang="en">
<head>
<meta charset="utf-8">
<title>Meadow Paws – business cards</title>
<link rel="stylesheet" href="https://fonts.googleapis.com/css2?family=Exo+2:wght@300;400;500&display=swap">
<style>
  :root {
    --brand-orange: #e3461e;
    --dog-tone: #e85a35;
    --ink: #1d1d1b;
    --paper: #ffffff;
    --page: #ffffff;
  }
  * { margin: 0; padding: 0; box-sizing: border-box; }
  html, body {
    width: 848px;
    height: 1200px;
    overflow: hidden;
    background: var(--page);
    font-family: "Exo 2", "Helvetica Neue", Arial, sans-serif;
  }
  .sheet { position: relative; width: 848px; height: 1200px; }

  .card {
    position: absolute;
    left: 140px;
    width: 584px;
    height: 327px;
    background: var(--brand-orange);
    box-shadow: 5px 5px 6px rgba(0, 0, 0, 0.35);
    overflow: hidden;
  }
  .card--front { top: 212px; }
  .card--back  { top: 656px; height: 328px; }

  .card__header {
    position: absolute;
    left: 0; top: 0;
    width: 100%;
    height: 86px;
    background: var(--paper);
  }
  .brand-name {
    position: absolute;
    left: 26px;
    top: 18px;
    font-size: 47px;
    line-height: 50px;
    font-weight: 400;
    letter-spacing: 0.5px;
    color: var(--brand-orange);
    text-transform: uppercase;
    white-space: nowrap;
  }
  .tagline {
    position: absolute;
    right: 32px;
    top: 48px;
    font-size: 16px;
    line-height: 18px;
    font-weight: 400;
    color: var(--ink);
  }

  .dog-artwork {
    position: absolute;
    left: 38px;
    top: 86px;
    width: 234px;
    height: 238px;
    border-radius: 40% 40% 8% 8%;
    background: radial-gradient(ellipse at 60% 40%, var(--dog-tone) 0%, var(--brand-orange) 75%);
  }

  .contact-phone,
  .contact-web {
    position: absolute;
    right: 32px;
    font-size: 28px;
    line-height: 30px;
    font-weight: 400;
    color: var(--paper);
    white-space: nowrap;
  }
  .contact-phone { top: 175px; }
  .contact-web   { top: 288px; }

  .services {
    position: absolute;
    left: 396px;
    top: 106px;
    list-style: none;
    color: var(--paper);
    font-size: 22px;
    line-height: 24px;
    font-weight: 400;
  }
  .services li {
    position: relative;
    padding-left: 12px;
    margin-bottom: 14px;
  }
  .services li::before {
    content: "";
    position: absolute;
    left: 0;
    top: 9px;
    width: 5px;
    height: 5px;
    background: var(--paper);
  }
</style>
</head>
<body>
<main class="sheet">

  <section class="card card--front" aria-label="Business card front">
    <header class="card__header">
      <div class="brand-name">Meadow Paws</div>
      <div class="tagline">happy hounds</div>
    </header>
    <div class="dog-artwork" role="img" aria-label="White line illustration of a seated bulldog"></div>
    <p class="contact-phone">Rua 049 830 71 64</p>
    <p class="contact-web">meadowpawsdemo.com.au</p>
  </section>

  <section class="card card--back" aria-label="Business card back">
    <header class="card__header">
      <div class="brand-name">Meadow Paws</div>
      <div class="tagline">happy hounds</div>
    </header>
    <div class="dog-artwork" role="img" aria-label="White line illustration of a seated bulldog"></div>
    <ul class="services">
      <li>walking</li>
      <li>holiday stays</li>
      <li>onsite care</li>
      <li>training</li>
      <li>behavioural<br>consultations</li>
    </ul>
  </section>

</main>
</body>
</html>
```